Hydraulics Company Business Card Design

Modern business card design for a hydraulics company.
Our company colours are - black, orange and white.
I would like the following contact details included-
Name
Position
Phone number
Email
Website
Street Address

I have attached our company logo.
I would like the back of the card white.

Thank you.

```html
<!DOCTYPE html>
<html lang="en">
<head>
<meta charset="utf-8">
<title>Tarrant Hydraulics – Business Card</title>
<link href="https://fonts.googleapis.com/css2?family=Montserrat:wght@600;700&family=Arimo:wght@400&display=swap" rel="stylesheet">
<style>
  :root {
    --backdrop: #2b2b2b;
    --card-black: #050505;
    --card-white: #ffffff;
    --orange: #f39a12;
    --text-light: #ffffff;
    --text-muted: #8c8c8c;
    --pattern-light: #f4f4f4;
    --pattern-mid: #e2e2e2;
  }
  * { margin: 0; padding: 0; box-sizing: border-box; }
  html, body {
    width: 1200px; height: 800px; overflow: hidden;
    background: var(--backdrop);
  }
  .stage { position: relative; width: 1200px; height: 800px; }
  .card {
    position: absolute; width: 560px; height: 320px;
    border-radius: 16px; overflow: hidden;
  }
  .card--front { left: 60px; top: 80px; background: var(--card-black); }
  .card--back  { left: 580px; top: 400px; background: var(--card-white); }

  .brand-name {
    font-family: "Montserrat", sans-serif; font-weight: 700;
    color: var(--orange); white-space: nowrap;
  }
  .card--front .brand-name {
    position: absolute; right: 34px; top: 34px; font-size: 26px;
  }
  .divider {
    position: absolute; left: 0; right: 0; top: 170px;
    height: 1px; background: var(--orange); opacity: .8;
  }
  .holder { position: absolute; left: 34px; top: 118px; }
  .holder-name {
    font-family: "Montserrat", sans-serif; font-weight: 600;
    font-size: 30px; color: var(--text-light); line-height: 1;
  }
  .holder-role {
    font-family: "Arimo", sans-serif; font-size: 15px;
    color: var(--text-muted); margin-top: 22px;
  }
  .contacts {
    position: absolute; left: 34px; bottom: 30px; list-style: none;
    font-family: "Arimo", sans-serif; font-size: 16px; color: var(--text-light);
  }
  .contacts li { display: flex; align-items: center; gap: 12px; height: 28px; }
  .contacts svg { width: 16px; height: 16px; fill: var(--orange); flex: none; }
  .address {
    position: absolute; right: 34px; top: 196px; text-align: right;
    font-family: "Arimo", sans-serif; font-size: 16px; line-height: 1.45;
    color: var(--text-light);
  }

  .back-pattern {
    position: absolute; inset: 0;
    background: linear-gradient(135deg, var(--pattern-mid) 0%, var(--pattern-light) 45%, var(--pattern-mid) 100%);
  }
  .card--back .brand-name {
    position: absolute; left: 300px; top: 176px; font-size: 20px;
  }
</style>
</head>
<body>
<main class="stage">
  <section class="card card--front" aria-label="Card front">
    <div class="brand-name">Tarrant Hydraulics</div>
    <div class="divider"></div>
    <div class="holder">
      <p class="holder-name">Dale Morrow</p>
      <p class="holder-role">Founder &amp; CEO</p>
    </div>
    <address class="address" style="font-style:normal">
      4410 Harbor Point Pkwy<br>212-B, FL 32541
    </address>
    <ul class="contacts">
      <li>
        <svg viewBox="0 0 16 16" aria-hidden="true"><path d="M3.5 1.5l2.5 0 1 3.5-1.6 1.2a8 8 0 0 0 4.4 4.4L11 9l3.5 1v2.5a2 2 0 0 1-2 2A11 11 0 0 1 1.5 3.5a2 2 0 0 1 2-2z"/></svg>
        044-987 654 321
      </li>
      <li>
        <svg viewBox="0 0 16 16" aria-hidden="true"><path d="M15 1L1 7l5 2 2 5z"/></svg>
        hello@tarranthyd.com
      </li>
      <li>
        <svg viewBox="0 0 16 16" aria-hidden="true"><path d="M8 1a7 7 0 1 0 0 14A7 7 0 0 0 8 1zm5.4 6.2h-2.5a11 11 0 0 0-1.2-4.6 5.6 5.6 0 0 1 3.7 4.6zM8 2.6c.8 1 1.4 2.7 1.5 4.6h-3c.1-1.9.7-3.6 1.5-4.6zM6.3 2.6a11 11 0 0 0-1.2 4.6H2.6a5.6 5.6 0 0 1 3.7-4.6zM2.6 8.8h2.5c.1 1.8.5 3.4 1.2 4.6a5.6 5.6 0 0 1-3.7-4.6zM8 13.4c-.8-1-1.4-2.7-1.5-4.6h3c-.1 1.9-.7 3.6-1.5 4.6zm1.7 0a11 11 0 0 0 1.2-4.6h2.5a5.6 5.6 0 0 1-3.7 4.6z"/></svg>
        www.tarranthyd.com
      </li>
    </ul>
  </section>

  <section class="card card--back" aria-label="Card back">
    <div class="back-pattern" role="img" aria-label="Repeating light grey company name pattern across the white card back"></div>
    <div class="brand-name">Tarrant Hydraulics</div>
  </section>
</main>
</body>
</html>
```